Silver Creek Plumbing Business card & letter head design

We need a new business card and letter head for our plumbing company called silver creek plumbing. attached is the companys logo. We provide domestic and commercial plumbing services in regional western Australia. We are after Something simple yet nice to look at and something that fits within the trade industry.

Target Market(s)

trade/building industry

Contact Information for Business Card

Darl Hensby
Manager
0461 238 574
enquiries@scplumbwork.net.au
ABN: 47 381 905 462
PCL: 5187

Domestic & Commercial Plumbing
Tip Truck & Excavator hire

Colors

Designer to choose colors to be used in the design.

```html
<!DOCTYPE html>
<html lang="en">
<head>
<meta charset="UTF-8">
<title>Silver Creek Plumbing – Business Card</title>
<link href="https://fonts.googleapis.com/css2?family=Montserrat:wght@400;500;700&family=Oswald:wght@600&display=swap" rel="stylesheet">
<style>
  :root {
    --backdrop: #4b4b4d;
    --card: #262627;
    --blue: #1b5fbb;
    --text: #e8e8e8;
    --muted: #cfcfcf;
  }
  * { box-sizing: border-box; margin: 0; padding: 0; }
  html, body {
    width: 1200px; height: 901px; overflow: hidden;
    background: var(--backdrop);
    font-family: "Montserrat", sans-serif;
    color: var(--text);
  }
  .sheet {
    width: 1200px; height: 901px;
    display: flex; flex-direction: column; align-items: center; justify-content: center;
    gap: 40px;
  }
  .card {
    position: relative;
    width: 640px; height: 366px;
    background: var(--card);
    box-shadow: 0 10px 30px rgba(0,0,0,.45);
    overflow: hidden;
  }
  .card__band {
    position: absolute; left: 0; right: 0; bottom: 0;
    height: 10px; background: var(--blue);
  }
  .tagline {
    position: absolute; left: 0; right: 0;
    text-align: center; font-size: 15px; line-height: 1.35;
    letter-spacing: .3px; color: var(--muted);
  }

  /* Front */
  .brand {
    position: absolute; top: 92px; left: 0; right: 0;
    display: flex; align-items: center; justify-content: center; gap: 14px;
  }
  .brand__dot {
    width: 22px; height: 22px; border-radius: 50%; background: var(--blue);
  }
  .brand__name {
    font-weight: 700; font-size: 34px; letter-spacing: 1px;
    text-transform: uppercase; color: var(--blue);
  }
  .brand__rule {
    position: absolute; top: 158px; left: 120px; right: 120px;
    height: 1px; background: var(--text);
  }
  .card--front .tagline { top: 206px; }

  /* Back */
  .identity {
    position: absolute; top: 96px; left: 50px; width: 230px;
    text-align: right;
  }
  .identity__name {
    font-family: "Oswald", sans-serif; font-weight: 600;
    font-size: 46px; line-height: 1; text-transform: uppercase;
    color: var(--blue); letter-spacing: .5px;
  }
  .identity__role { font-size: 17px; margin-top: 6px; color: var(--muted); }
  .divider {
    position: absolute; top: 84px; left: 300px;
    width: 2px; height: 118px; background: var(--blue);
  }
  .contact {
    position: absolute; top: 88px; left: 322px;
    font-size: 16px; line-height: 1.45; color: var(--text);
  }
  .contact__row { display: flex; align-items: center; gap: 10px; }
  .contact__row--gap { margin-top: 8px; }
  .contact__icon { width: 16px; height: 16px; fill: var(--blue); flex: none; }
  .card--back .tagline { top: 262px; }
</style>
</head>
<body>
<main class="sheet">
  <section class="card card--front" aria-label="Business card front">
    <div class="brand">
      <span class="brand__dot"></span>
      <span class="brand__name">Silver Creek Plumbing</span>
    </div>
    <div class="brand__rule"></div>
    <p class="tagline">Domestic &amp; Commercial Plumbing<br>Tip Truck &amp; Excavator hire</p>
    <div class="card__band"></div>
  </section>

  <section class="card card--back" aria-label="Business card back">
    <div class="identity">
      <h1 class="identity__name">Darl Hensby</h1>
      <p class="identity__role">Manager</p>
    </div>
    <div class="divider"></div>
    <div class="contact">
      <p>ABN: 47 381 905 462</p>
      <p>PCL: 5187</p>
      <p class="contact__row contact__row--gap">
        <svg class="contact__icon" viewBox="0 0 24 24" aria-hidden="true"><path d="M6.6 10.8c1.4 2.8 3.8 5.1 6.6 6.6l2.2-2.2c.3-.3.7-.4 1-.2 1.1.4 2.3.6 3.6.6.6 0 1 .4 1 1V20c0 .6-.4 1-1 1C10.6 21 3 13.4 3 4c0-.6.4-1 1-1h3.5c.6 0 1 .4 1 1 0 1.3.2 2.5.6 3.6.1.3 0 .7-.2 1z"/></svg>
        0461 238 574
      </p>
      <p class="contact__row">
        <svg class="contact__icon" viewBox="0 0 24 24" aria-hidden="true"><path d="M2 5h20v14H2z M4 7v.5l8 5 8-5V7l-8 5z" fill-rule="evenodd"/></svg>
        enquiries@scplumbwork.net.au
      </p>
    </div>
    <p class="tagline">Domestic &amp; Commercial Plumbing<br>Tip Truck &amp; Excavator hire</p>
    <div class="card__band"></div>
  </section>
</main>
</body>
</html>
```